CORPORATE AND CLASSY CHRISTMAS CARD (CONTEST)

We want a Christmas card for wealth managers to issue to high net worth clients. Very classy (the target market is clients with investments - typically more than £100,000 which is why the card needs to be very classy). Very corporate. The finished printed card will be a5 to fit existing envelopes. The design will also be used as part of a digital card so i need the image in a format for email as well as print. The brand uses a silver (foil block) on its logo and a specific pan tone ref olive green (reference 620). Not too religious and include a quirky message.

Target Market(s)

High net worth clients - clients with investments, typically more than £100,000 which is why the card needs to be very classy

Requirements
Must have
• The image in a format for email as well as print.
Nice to have
• Very corporate, very classy, the colour scheme of the brand - silver (foil block) and a specific pan ton ref olive green (ref 620) used in a quirky and different way
Should not have
• not too religious

```html
<!DOCTYPE html>
<html lang="en">
<head>
<meta charset="utf-8">
<title>Season's Greetings Card</title>
<link href="https://fonts.googleapis.com/css2?family=Cinzel:wght@400&family=Great+Vibes&display=swap" rel="stylesheet">
<style>
  :root {
    --olive: #8b7c2d;
    --paper: #ffffff;
    --silver-light: #e6e6e6;
    --silver-mid: #a9a9a9;
    --silver-dark: #5f5f5f;
    --message-grey: #9b9b9b;
  }
  html, body {
    margin: 0;
    padding: 0;
    overflow: hidden;
    background: var(--paper);
  }
  .card {
    position: relative;
    width: 847px;
    height: 1200px;
    background: var(--paper);
    overflow: hidden;
  }
  .greeting {
    position: absolute;
    left: 0;
    top: 0;
    width: 847px;
    height: 400px;
    margin: 0;
    font-weight: 400;
  }
  .silver {
    background: linear-gradient(180deg, var(--silver-light) 0%, var(--silver-mid) 45%, var(--silver-dark) 70%, var(--silver-mid) 100%);
    -webkit-background-clip: text;
    background-clip: text;
    color: transparent;
  }
  .initial {
    position: absolute;
    font-family: "Great Vibes", cursive;
    line-height: 1;
    padding: 20px 40px;
  }
  .initial-s { left: 0; top: 0; font-size: 230px; }
  .initial-g { left: -20px; top: 128px; font-size: 220px; }
  .caps {
    position: absolute;
    font-family: "Cinzel", serif;
    line-height: 1;
    white-space: nowrap;
  }
  .caps-eason { left: 214px; top: 128px; font-size: 84px; letter-spacing: 7px; }
  .caps-reetings { left: 200px; top: 256px; font-size: 82px; letter-spacing: 3px; }

  .tree {
    position: absolute;
    fill: var(--olive);
  }
  .tree-top { left: 626px; top: 244px; width: 150px; height: 158px; }
  .tree-bottom { left: 656px; top: 1062px; width: 96px; height: 100px; }

  .band {
    position: absolute;
    left: 0;
    width: 847px;
    background: var(--olive);
  }
  .band-main { top: 400px; height: 200px; }
  .band-foot { top: 1160px; height: 40px; }

  .message {
    position: absolute;
    left: 0;
    top: 770px;
    width: 847px;
    margin: 0;
    text-align: center;
    font-family: "Cinzel", serif;
    font-size: 60px;
    line-height: 71px;
    letter-spacing: 1px;
    color: var(--message-grey);
  }
</style>
</head>
<body>
<main class="card">
  <h1 class="greeting" aria-label="Season's Greetings">
    <span class="initial initial-s silver" aria-hidden="true">S</span>
    <span class="caps caps-eason silver" aria-hidden="true">EASON'S</span>
    <span class="initial initial-g silver" aria-hidden="true">G</span>
    <span class="caps caps-reetings silver" aria-hidden="true">REETINGS</span>
  </h1>

  <svg class="tree tree-top" viewBox="0 0 72 76" aria-hidden="true">
    <polygon points="36,0 38,5 43,5 39,8 40.5,13 36,10 31.5,13 33,8 29,5 34,5"/>
    <polygon points="36,11 47,27 42,27 55,42 49,42 64,58 72,60 50,62 22,62 0,60 8,58 23,42 17,42 30,27 25,27"/>
    <rect x="32" y="61" width="8" height="15"/>
  </svg>
  <div class="band band-main"></div>

  <p class="message">Sending you the<br>warmest wishes in<br>the new year!</p>

  <svg class="tree tree-bottom" viewBox="0 0 72 76" aria-hidden="true">
    <polygon points="36,0 38,5 43,5 39,8 40.5,13 36,10 31.5,13 33,8 29,5 34,5"/>
    <polygon points="36,11 47,27 42,27 55,42 49,42 64,58 72,60 50,62 22,62 0,60 8,58 23,42 17,42 30,27 25,27"/>
    <rect x="32" y="61" width="8" height="15"/>
  </svg>
  <div class="band band-foot"></div>
</main>
</body>
</html>
```